Brightvale services brochure

We need a new company brochure. The brochure will be formatted for PDF distribution but should be printable on "letter" size paper. 2 pages plus front and back cover. Color white and same blue as logo. Logo "O" should be used as design. Look at webpage for general info: www.brightvale-example.ca<br/><br/>Front cover: pic1, logo, design and "Your Cleaning is Our Business". <br/>Back cover" "O" design, logo and info from "contact" page<br/>Front cover inside: design and intro from web home page, also use stock pics of clean offices ect as placeholders for purchased pics.<br/>1st page: design and "Our Services", use info of "Cleanroom & GMP Services", "Janitorial Services" from services page.<br/>2nd page: design and "Special Services", info from "Carpet & Upholstery Services", "Window Cleaning Services", and list of "Other Services".<br/>Back cover inside : design and info from technology page, use stock pics for place holders.

Industry/Entity Type

Janitorial

Font styles to use
Sans Serif
Other font styles liked:
• Futura Book

Colors
0555a3

Requirements
Must have
• The logo "O" (target) should be part of the design. Design color same as logo.

```html
<!DOCTYPE html>
<html lang="en">
<head>
<meta charset="utf-8">
<title>Brightvale services brochure</title>
<link href="https://fonts.googleapis.com/css2?family=Montserrat:wght@400;500;600;700;800&display=swap" rel="stylesheet">
<style>
:root{
  --blue:#0a7cc4;
  --blue-deep:#0555a3;
  --blue-light:#3fa3e0;
  --ink:#1d1d1f;
  --muted:#5a6470;
  --paper:#ffffff;
  --paper-shade:#f1f3f5;
  --stage:#2e2f31;
}
*{box-sizing:border-box;margin:0;padding:0}
html,body{width:960px;height:1200px;overflow:hidden;background:var(--stage)}
body{font-family:"Montserrat",Arial,sans-serif;color:var(--ink);position:relative}
.spread{position:absolute;left:20px;width:920px;height:580px;display:flex;box-shadow:0 6px 18px rgba(0,0,0,.45)}
.spread--outer{top:20px}
.spread--inner{top:620px}
.page{position:relative;width:460px;height:580px;background:var(--paper);overflow:hidden}
.page + .page{border-left:1px solid #dde1e5}
.page svg.art{position:absolute;left:0;top:0;width:460px;height:580px}
.wordmark{font-weight:600;color:var(--blue);letter-spacing:.18em;display:flex;align-items:center;gap:8px}
.wordmark::before{content:"";width:10px;height:10px;border-radius:50%;background:var(--blue)}

/* back cover */
.availability{position:absolute;left:40px;top:320px;width:400px;color:#fff;transform:rotate(-14deg);transform-origin:left top}
.availability p{font-weight:600;font-size:15px;letter-spacing:.04em;line-height:1.35;text-transform:uppercase}
.availability strong{font-weight:800;font-size:17px}
.availability .hours{position:absolute;left:230px;top:-34px;font-weight:800;font-style:normal;font-size:44px;letter-spacing:-.02em}
.contact{position:absolute;left:40px;top:455px}
.contact h2{font-size:14px;font-weight:700;letter-spacing:.03em;margin-bottom:10px}
.contact h2 span{color:var(--blue)}
.contact h2::after{content:"";display:block;width:22px;height:2px;background:var(--blue);margin-top:4px}
.contact li{list-style:none;display:flex;align-items:center;gap:8px;font-size:11.5px;font-weight:500;line-height:1.75}
.contact li svg{width:11px;height:11px;flex:none}
.back-mark{position:absolute;right:36px;top:470px;font-size:15px}

/* front cover */
.front-mark{position:absolute;left:0;right:0;top:42px;justify-content:center;font-size:26px}
.tagline{position:absolute;left:0;right:0;top:380px;text-align:center;color:#fff;transform:rotate(-7deg)}
.tagline .lead{font-weight:500;font-size:16px;letter-spacing:.28em}
.tagline .main{font-weight:800;font-size:34px;letter-spacing:.04em}
.front-url{position:absolute;left:0;right:0;top:522px;text-align:center;font-size:10px;font-weight:600;letter-spacing:.22em;color:var(--ink)}
.front-url span{color:var(--blue)}

/* inner pages */
.section-title{position:absolute;font-size:19px;letter-spacing:.28em;font-weight:500;display:flex;align-items:center;gap:10px;text-transform:uppercase}
.section-title::before{content:"";width:3px;height:18px;background:var(--blue)}
.section-title span{color:var(--blue);font-weight:600}
.services{position:absolute;left:34px;top:82px;width:400px;list-style:none}
.service{display:flex;gap:14px;align-items:center;height:62px}
.service-icon{width:46px;height:46px;flex:none;border-radius:50%;background:radial-gradient(circle at 40% 35%,#ffffff 0%,#e6edf3 70%);box-shadow:3px 3px 6px rgba(0,0,0,.18);position:relative}
.service-icon i{position:absolute;inset:12px;border-radius:50%;background:linear-gradient(135deg,var(--blue-light),var(--blue-deep))}
.service h3{font-size:13px;font-weight:600;color:var(--blue-deep);margin-bottom:3px}
.service p{font-size:8.5px;line-height:1.35;color:var(--muted)}
.program{position:absolute;left:34px;top:462px;width:400px;color:#fff;padding-left:14px;border-left:3px solid #fff}
.program h3{font-size:13px;font-weight:600;line-height:1.3;text-transform:uppercase;margin-bottom:6px}
.program p{font-size:10px;line-height:1.45;opacity:.95}
.program b{font-weight:700}

.other-list{position:absolute;left:34px;top:74px;list-style:none}
.other-list li{font-size:11px;font-weight:500;line-height:18.5px;display:flex;gap:8px}
.other-list li::before{content:"»";color:var(--blue);font-weight:700}
.portrait{position:absolute;left:305px;top:22px;width:138px;height:138px;border-radius:50%;border:2px solid var(--blue);padding:4px}
.portrait div{width:100%;height:100%;border-radius:50%;background:radial-gradient(circle at 55% 40%,#f4e9df 0%,#dcd6cf 35%,#b9c6d2 70%,#e9c24a 100%)}
.offers-bar{position:absolute;left:24px;top:352px;width:412px;height:28px;background:#fff;border-radius:3px;text-align:center;font-weight:700;font-size:14px;line-height:28px;letter-spacing:.04em}
.offers{position:absolute;left:24px;top:396px;display:flex;gap:10px}
.offer{width:95px;height:108px;background:#fff;border-radius:3px;text-align:center;box-shadow:0 3px 8px rgba(0,0,0,.25);display:flex;flex-direction:column}
.offer .top{height:34px;display:flex;align-items:center;justify-content:center;font-size:9px;font-weight:500;line-height:1.2;padding:0 6px}
.offer .value{background:var(--blue-deep);color:#fff;font-weight:800;font-size:20px;letter-spacing:.04em;height:32px;line-height:32px}
.offer .note{flex:1;display:flex;align-items:center;justify-content:center;font-size:8px;font-weight:500;line-height:1.2;text-transform:uppercase;padding:0 6px}
</style>
</head>
<body>

<section class="spread spread--outer">
  <!-- back cover -->
  <article class="page page--back-cover">
    <svg class="art" viewBox="0 0 460 580" aria-hidden="false">
      <defs>
        <linearGradient id="wipeTones" x1="0" y1="0" x2="1" y2="1">
          <stop offset="0" stop-color="#e8eef3"/>
          <stop offset=".35" stop-color="#3b8fd6"/>
          <stop offset=".6" stop-color="#a4552a"/>
          <stop offset="1" stop-color="#f2f2f2"/>
        </linearGradient>
        <linearGradient id="bandBack" x1="0" y1="0" x2="1" y2="0">
          <stop offset="0" stop-color="var(--blue)"/>
          <stop offset="1" stop-color="var(--blue-deep)"/>
        </linearGradient>
      </defs>
      <path d="M0,0 H460 V190 Q300,360 0,285 Z" fill="url(#wipeTones)" role="img" aria-label="Photo: gloved hand wiping a wooden surface with a cloth"/>
      <path d="M0,285 Q300,360 460,190 V285 Q330,470 0,425 Z" fill="url(#bandBack)"/>
    </svg>
    <div class="availability">
      <span class="hours">24/7</span>
      <p><strong>At Brightvale</strong><br>We are available<br>for supporting our clients.</p>
    </div>
    <div class="contact">
      <h2>CONTACT <span>BRIGHTVALE</span></h2>
      <ul>
        <li><svg viewBox="0 0 12 12"><path d="M3 1 L5 3 L4 4.5 Q5 7 7.5 8 L9 7 L11 9 L9.5 11 Q3 10 1 2.5 Z" fill="var(--blue)"/></svg>1 (866) 555-0142</li>
        <li><svg viewBox="0 0 12 12"><path d="M3 1 L5 3 L4 4.5 Q5 7 7.5 8 L9 7 L11 9 L9.5 11 Q3 10 1 2.5 Z" fill="var(--blue)"/></svg>(905) 555-0187</li>
        <li><svg viewBox="0 0 12 12"><rect x="1" y="2.5" width="10" height="7" rx="1" fill="none" stroke="var(--blue)" stroke-width="1.3"/><path d="M1.5 3 L6 6.5 L10.5 3" fill="none" stroke="var(--blue)" stroke-width="1.3"/></svg>info@brightvale-example.ca</li>
        <li><svg viewBox="0 0 12 12"><circle cx="6" cy="6" r="4.8" fill="none" stroke="var(--blue)" stroke-width="1.3"/><path d="M1.2 6 H10.8 M6 1.2 Q3 6 6 10.8 M6 1.2 Q9 6 6 10.8" fill="none" stroke="var(--blue)" stroke-width="1"/></svg>www.brightvale-example.ca</li>
      </ul>
    </div>
    <div class="wordmark back-mark">BRIGHTVALE</div>
  </article>

  <!-- front cover -->
  <article class="page page--front-cover">
    <svg class="art" viewBox="0 0 460 580">
      <defs>
        <linearGradient id="towerTones" x1="0" y1="0" x2="0" y2="1">
          <stop offset="0" stop-color="#f4f7fa"/>
          <stop offset=".45" stop-color="#9fb4c4"/>
          <stop offset=".8" stop-color="#6f8a96"/>
          <stop offset="1" stop-color="#4e7a46"/>
        </linearGradient>
        <linearGradient id="bandFront" x1="0" y1="0" x2="1" y2="1">
          <stop offset="0" stop-color="var(--blue-light)"/>
          <stop offset="1" stop-color="var(--blue-deep)"/>
        </linearGradient>
      </defs>
      <path d="M0,230 Q220,420 460,240 V440 Q250,540 0,480 Z" fill="url(#bandFront)"/>
      <path d="M40,95 H460 V240 Q250,410 40,290 Z" fill="url(#towerTones)" role="img" aria-label="Photo: modern glass office tower with trees at its base"/>
    </svg>
    <div class="wordmark front-mark">BRIGHTVALE</div>
    <div class="tagline">
      <div class="lead">YOUR CLEANING IS</div>
      <div class="main">OUR BUSINESS</div>
    </div>
    <div class="front-url">www.<span>brightvale-example</span>.ca</div>
  </article>
</section>

<section class="spread spread--inner">
  <!-- page one -->
  <article class="page page--services">
    <svg class="art" viewBox="0 0 460 580">
      <defs>
        <linearGradient id="bandInnerLeft" x1="0" y1="0" x2="1" y2="0">
          <stop offset="0" stop-color="var(--blue-deep)"/>
          <stop offset="1" stop-color="var(--blue-light)"/>
        </linearGradient>
      </defs>
      <path d="M0,440 Q240,390 460,372 V392 Q240,410 0,452 Z" fill="#c9ced3"/>
      <path d="M0,448 Q240,405 460,388 V580 H0 Z" fill="url(#bandInnerLeft)"/>
    </svg>
    <h2 class="section-title" style="left:34px;top:40px">Our <span>Services</span></h2>
    <ul class="services">
      <li class="service"><div class="service-icon" role="img" aria-label="Icon: janitor with cleaning cart"><i></i></div><div><h3>Janitorial Services</h3><p>Brightvale delivers complete janitorial care for offices, schools, plants, showrooms, churches and apartment buildings of any size.</p></div></li>
      <li class="service"><div class="service-icon" role="img" aria-label="Icon: worker with mop and bucket"><i></i></div><div><h3>Cleanroom &amp; GMP Services</h3><p>A trusted name in cleanroom care with proven procedures, trained staff and technology for demanding regulated facilities.</p></div></li>
      <li class="service"><div class="service-icon" role="img" aria-label="Icon: worker vacuuming carpet"><i></i></div><div><h3>Carpet &amp; Upholstery Services</h3><p>Carpets, drapes and upholstered furniture are an investment; we keep them clean and extend their lifespan.</p></div></li>
      <li class="service"><div class="service-icon" role="img" aria-label="Icon: worker cleaning a window"><i></i></div><div><h3>Window Cleaning Services</h3><p>Regular or project-based interior and exterior window cleaning for high-rise and low-level buildings alike.</p></div></li>
      <li class="service"><div class="service-icon" role="img" aria-label="Icon: worker restoring a damaged floor"><i></i></div><div><h3>Fire And Flood Restoration Services</h3><p>When fire, flood or vandalism strikes, we restore your building quickly so tenants can return sooner.</p></div></li>
    </ul>
    <div class="program">
      <h3>Special 2019<br>Novel Coronavirus Disinfecting Program</h3>
      <p>With the global spreading of the 2019 <b>Novel Coronavirus (2019-nCoV)</b>, Brightvale offers preventive disinfecting programs to ensure facilities are properly disinfected. Contact us for a program that fits your needs.</p>
    </div>
  </article>

  <!-- page two -->
  <article class="page page--other-services">
    <svg class="art" viewBox="0 0 460 580">
      <defs>
        <linearGradient id="bandInnerRight" x1="0" y1="0" x2="1" y2="1">
          <stop offset="0" stop-color="var(--blue)"/>
          <stop offset="1" stop-color="var(--blue-deep)"/>
        </linearGradient>
        <linearGradient id="greySweep" x1="0" y1="0" x2="1" y2="0">
          <stop offset="0" stop-color="#ffffff"/>
          <stop offset="1" stop-color="#8e969e"/>
        </linearGradient>
      </defs>
      <path d="M0,330 Q220,268 460,262 V300 Q230,300 0,350 Z" fill="url(#greySweep)"/>
      <path d="M0,345 Q230,292 460,292 V580 H0 Z" fill="url(#bandInnerRight)"/>
    </svg>
    <h2 class="section-title" style="left:30px;top:40px">Other <span>Services</span></h2>
    <ul class="other-list">
      <li>Day Porter Services</li>
      <li>Construction Clean-Ups</li>
      <li>Quality Control Inspections</li>
      <li>Maid Services</li>
      <li>Light &amp; Ceiling Fixture Cleaning</li>
      <li>Wall Washing</li>
      <li>Drapery &amp; Blind Cleaning</li>
      <li>Acoustical Tile Cleaning</li>
      <li>Computer Terminal, Monitor and Keyboard Cleaning</li>
      <li>Marble, Granite &amp; Terrazzo Refinishing &amp; Maintenance</li>
      <li>Power Washing</li>
    </ul>
    <div class="portrait"><div role="img" aria-label="Photo: cleaner in yellow gloves washing a window"></div></div>
    <div class="offers-bar">OUR SPECIAL OFFERS</div>
    <div class="offers">
      <div class="offer"><div class="top">All Estimates</div><div class="value">FREE</div><div class="note"></div></div>
      <div class="offer"><div class="top">New Janitorial Contracts</div><div class="value">FREE</div><div class="note">Carpet Cleaning</div></div>
      <div class="offer"><div class="top">Janitorial Supplies</div><div class="value">FREE</div><div class="note">Delivery</div></div>
      <div class="offer"><div class="top">Starting at</div><div class="value">$95</div><div class="note">Carpet Maintenance Program</div></div>
    </div>
  </article>
</section>

</body>
</html>
```